Business Card Design for Animal Clinic

We are seeking a two sided business card design. The primary side should include our logo (provided in AI and EPS files) address, phone, website, and if possible "Follow Us" with icons for Facelog, Circlesphere, and Chirpline.

The back of the card needs to included space for appointment reminders.

Company Name:
Brackenfield Animal Clinic

Doctor Name:
To be provided to winner

Adress:
To be provided to winner

Phone:
to be provided to winner

Website:
www.brackenfieldanimalclinic.example

```html
<!DOCTYPE html>
<html lang="en">
<head>
<meta charset="utf-8">
<title>Brackenfield Animal Clinic – Business Card</title>
<link rel="stylesheet" href="https://fonts.googleapis.com/css2?family=Questrial&display=swap">
<style>
  :root {
    --card-grey: #e5e3e0;
    --clinic-red: #a52a22;
    --clinic-rust: #c8704f;
    --divider: #d09a7e;
    --ink: #1c1c1c;
    --ghost: #e0cbc3;
    --paper: #ffffff;
  }
  * { margin: 0; padding: 0; box-sizing: border-box; }
  html, body {
    width: 850px; height: 1200px; overflow: hidden;
    background: var(--paper);
    font-family: "Questrial", "Century Gothic", sans-serif;
  }
  .canvas { position: relative; width: 850px; height: 1200px; }

  /* Front side */
  .card-front {
    position: absolute; left: 0; top: 0; width: 850px; height: 554px;
    background: var(--card-grey);
  }
  .brand {
    position: absolute; left: 0; top: 58px; width: 850px;
    text-align: center; color: var(--clinic-red);
  }
  .brand-name { font-size: 58px; letter-spacing: 2px; line-height: 1; }
  .brand-sub { font-size: 28px; letter-spacing: 4px; margin-top: 30px; }

  .contact-divider {
    position: absolute; left: 422px; top: 273px; width: 3px; height: 140px;
    background: var(--divider);
  }
  .contact { position: absolute; font-size: 27px; color: var(--ink); line-height: 1; }
  .contact-left { right: 444px; text-align: right; }
  .contact-right { left: 441px; }
  .row-1 { top: 292px; }
  .row-2 { top: 350px; }

  .social {
    position: absolute; right: 30px; top: 484px;
    display: flex; align-items: center; gap: 12px; color: var(--ink);
  }
  .social-label { font-size: 27px; margin-right: 4px; }
  .social-network { font-size: 16px; color: var(--clinic-red); }

  /* Back side */
  .card-back {
    position: absolute; left: 0; top: 647px; width: 850px; height: 553px;
    background: var(--clinic-red);
  }
  .reminder-panel {
    position: absolute; left: 20px; top: 19px; width: 811px; height: 515px;
    background: var(--card-grey); border-radius: 57px; overflow: hidden;
  }
  .ghost-brand {
    position: absolute; left: 0; top: 110px; width: 811px;
    text-align: center; color: var(--ghost);
  }
  .ghost-name { font-size: 108px; letter-spacing: 2px; line-height: 1; }
  .ghost-sub { font-size: 54px; letter-spacing: 6px; margin-top: 60px; }
  .reminder-line {
    position: absolute; left: 57px; width: 690px; height: 0;
    border-top: 2px dotted var(--ink);
  }
</style>
</head>
<body>
<div class="canvas">
  <section class="card-front">
    <div class="brand">
      <div class="brand-name">BRACKENFIELD</div>
      <div class="brand-sub">ANIMAL CLINIC</div>
    </div>

    <div class="contact contact-left row-1">Dr. Name</div>
    <div class="contact contact-left row-2">Adress</div>
    <div class="contact-divider"></div>
    <div class="contact contact-right row-1">Phone</div>
    <div class="contact contact-right row-2">website</div>

    <div class="social">
      <span class="social-label">follow us</span>
      <span class="social-network">Chirpline</span>
      <span class="social-network">Facelog</span>
      <span class="social-network">Circlesphere</span>
    </div>
  </section>

  <section class="card-back">
    <div class="reminder-panel">
      <div class="ghost-brand" aria-hidden="true">
        <div class="ghost-name">BRACKENFIELD</div>
        <div class="ghost-sub">ANIMAL CLINIC</div>
      </div>
      <div class="reminder-line" style="top:117px"></div>
      <div class="reminder-line" style="top:202px"></div>
      <div class="reminder-line" style="top:286px"></div>
      <div class="reminder-line" style="top:370px"></div>
      <div class="reminder-line" style="top:454px"></div>
    </div>
  </section>
</div>
</body>
</html>
```